New Slide Master Template for PPT

I need a new Slide Master / Template for PPT presentations. Our company does Cloud Management / Network Management systems that are used to manage devices connected to the internet. Those devices can be things like Wireless Access Points, DSL modems, Cable modems, Gateways, Routers, Switches, and the equipment that is in the internet such as Brevok, Talsome, or Ormavin-Dusk equipment.
What our management system does is connect/communicate with all these different devices to be able to get information from the devices such as throughput performance, wireless coverage, failures conditions, firmware versions, and any other information which is used to manage, control, or troubleshoot those devices for the equipment companies or internet service providers who have provided them to their end customers for internet service.
The new Slide Master / Template for PowerPoint needs to do to the following;
1. be fresh and current in design
2. have a nice looking font that works for both print and presentation on small screens (laptops) as well as big screen (large group presentations)
3. not consume too many MegaBytes when saved as a file. Many email servers have limits on the size of files which can be transferred as an attachment. Most are either 5 or 10 MB limits. I do not want to have to zip the file to get it under such size restrictions.
4. the colors in the "Quorvian" logo are the company colors (the orange and blue), those should be incorporated in some form in the Slide Master / Template.
5. the final design should communicate professionalism with a modern look and feel.
6. once done the attached (old version of presentation) should be transferred over using the new Slide Master / Template and new fonts.
NOTE: I am not seeing how to attach my current PPT file to this project. Please email me at tobias@fernpathsystems.example and I will send you the current presentation which needs to be updated as described above.
Updates
Target Market(s)
Networking equipment manufacturers like Brevok, Pylorn, Ormavin-Dusk, VoxTe, etc.
Industry/Entity Type
Internet
Look and feel
Each slider illustrates characteristics of the customer's brand and the style your logo design should communicate.

```html
<!DOCTYPE html>
<html lang="en">
<head>
<meta charset="utf-8">
<title>Quorvian Slide Master</title>
<link href="https://fonts.googleapis.com/css2?family=Ubuntu:wght@400;500;700&display=swap" rel="stylesheet">
<style>
:root{
  --blue:#1a7fd4;
  --blue-dark:#1466b0;
  --orange:#f5b800;
  --ink:#2b2b2b;
  --grey:#8c8c8c;
  --rule:#b9d6f0;
  --stage:#d9d9d9;
}
*{box-sizing:border-box;margin:0;padding:0}
html,body{width:1200px;height:900px;overflow:hidden}
body{background:radial-gradient(ellipse at center,#f4f4f4 0%,var(--stage) 100%);font-family:"Ubuntu",sans-serif;color:var(--ink);position:relative}
.slide{position:absolute;width:373px;height:280px;background:#fff;box-shadow:2px 3px 6px rgba(0,0,0,.35);overflow:hidden}
.c1{left:28px}.c2{left:414px}.c3{left:800px}
.r1{top:15px}.r2{top:309px}.r3{top:603px}
.brand{display:flex;align-items:center;gap:5px;font-weight:700;color:var(--blue)}
.brand .dot{border-radius:50%;background:var(--orange)}
.band{position:absolute;left:0;width:100%;background:var(--blue);color:#fff;text-align:center}
.band h1{font-size:12.5px;font-weight:500;margin-top:12px}
.band p{font-size:6.5px;margin-top:8px}
.url{font-size:5px;letter-spacing:1px}
.copyright{position:absolute;bottom:5px;left:0;width:100%;text-align:center;font-size:3.5px;color:var(--blue)}
.slide-title{position:absolute;left:23px;top:20px;right:21px;font-size:12.5px;color:var(--blue);border-bottom:1px solid var(--rule);padding-bottom:2px}
.footer-brand{position:absolute;left:20px;bottom:8px;font-size:7.5px}
.footer-brand .dot{width:7px;height:7px}
.page-no{position:absolute;right:20px;bottom:5px;font-size:4px;color:var(--blue)}
.bullets{list-style:none;font-size:5.5px;line-height:1.6}
.bullets li{position:relative;padding-left:7px}
.bullets li::before{content:"•";position:absolute;left:0;color:var(--blue)}
svg text{font-family:"Ubuntu",sans-serif}
</style>
</head>
<body>

<!-- Title slide with photo -->
<section class="slide c1 r1">
  <div role="img" aria-label="Black and white photograph of bare feet walking on a sandy beach" style="position:absolute;inset:0;background:linear-gradient(180deg,#1e1e1e 0%,#5a5a5a 35%,#9a9a9a 60%,#4a4a4a 100%)"></div>
  <div style="position:absolute;left:0;top:78px;width:100%;height:59px;background:rgba(190,190,190,.85);display:flex;align-items:center;justify-content:center">
    <div class="brand" style="font-size:15px;color:#1f1f1f"><span class="dot" style="width:12px;height:12px"></span>Quorvian</div>
  </div>
  <div class="band" style="top:201px;height:50px">
    <h1>Insert The Title of Your Presentation Here</h1>
    <p>Subtitle of the Presentation or main author's name here</p>
  </div>
  <div class="url" style="position:absolute;bottom:4px;width:100%;text-align:center;color:#fff">www.quorvian.example</div>
</section>

<!-- Title slide, light -->
<section class="slide c2 r1">
  <div style="position:absolute;left:120px;top:46px;width:132px;height:132px;border-radius:50%;background:radial-gradient(circle at 50% 40%,#fafafa 0%,#e4e4e4 100%);display:flex;flex-direction:column;align-items:center;justify-content:center;gap:18px">
    <div class="brand" style="font-size:15px;color:#1f1f1f"><span class="dot" style="width:12px;height:12px"></span>Quorvian</div>
    <div class="url" style="color:#aaa">www.quorvian.example</div>
  </div>
  <div class="band" style="top:200px;height:50px">
    <h1>Insert The Title of Your Presentation Here</h1>
    <p>Subtitle of the Presentation or main author's name here</p>
  </div>
  <div class="copyright">© 2013 Quorvian Technologies. All rights reserved</div>
</section>

<!-- Agenda -->
<section class="slide c3 r1" style="background:var(--blue);color:#fff">
  <h2 style="position:absolute;left:23px;top:56px;font-size:15px;font-weight:500">Agenda</h2>
  <ul class="bullets" style="position:absolute;left:20px;top:80px;width:354px;font-size:6.5px;line-height:1.85">
    <li style="border:1px solid #9cc8ef;border-radius:2px;width:334px;padding-left:9px;margin-left:-2px">Chapter 1</li>
    <li>Chapter 2</li>
    <li>Chapter 3</li>
  </ul>
  <div style="position:absolute;left:3px;bottom:7px;width:57px;height:20px;background:#fff;display:flex;align-items:center;justify-content:center">
    <div class="brand" style="font-size:7px"><span class="dot" style="width:6px;height:6px"></span>Quorvian</div>
  </div>
</section>

<!-- Text slide -->
<section class="slide c1 r2">
  <h2 class="slide-title" style="font-weight:400">Text slide</h2>
  <ul class="bullets" style="position:absolute;left:23px;top:54px;width:330px;display:flex;flex-direction:column;gap:10px">
    <li>Lorem ipsum dolor sit amet, consectetur adipiscing elit. Duis blandit lorem eu libero congue aliquam vel sit amet augue. Mauris augue ipsum, dignissim vitae adipiscing eu, euismod nec sem.</li>
    <li>Lorem ipsum dolor sit amet, consectetur adipiscing elit. Duis blandit lorem eu libero congue aliquam vel sit amet augue. Mauris augue ipsum, dignissim vitae adipiscing eu, euismod nec sem.</li>
    <li>Lorem ipsum dolor sit amet, consectetur adipiscing elit. Duis blandit lorem eu libero congue aliquam vel sit amet augue. Mauris augue ipsum, dignissim vitae adipiscing eu, euismod nec sem.</li>
    <li>Lorem ipsum dolor sit amet, consectetur adipiscing elit. Duis blandit lorem eu libero congue aliquam vel sit amet augue. Mauris augue ipsum, dignissim vitae adipiscing eu, euismod nec sem.</li>
    <li>Lorem ipsum dolor sit amet, consectetur adipiscing elit. Duis blandit lorem eu libero congue aliquam vel sit amet augue. Mauris augue ipsum, dignissim vitae adipiscing eu, euismod nec sem.</li>
    <li>Lorem ipsum dolor sit amet, consectetur adipiscing elit. Duis blandit lorem eu libero congue aliquam vel sit amet augue. Mauris augue ipsum, dignissim vitae adipiscing eu, euismod nec sem.</li>
  </ul>
  <div class="brand footer-brand"><span class="dot"></span>Quorvian</div>
  <div class="copyright">© 2013 Quorvian Technologies. All rights reserved</div>
  <div class="page-no">4</div>
</section>

<!-- Graph slide 1: bars -->
<section class="slide c2 r2">
  <h2 class="slide-title" style="font-weight:400">Graph Slide – Example 1</h2>
  <svg width="373" height="280" style="position:absolute;left:0;top:0" aria-label="Bar chart by quarter">
    <text x="105" y="83" font-size="5.5" fill="#333" text-anchor="middle">Graph</text>
    <line x1="62" y1="92" x2="62" y2="232" stroke="#ccc" stroke-width=".6"/>
    <g font-size="5.5" fill="#333">
      <text x="56" y="110" text-anchor="end">1st Qtr</text>
      <rect x="62" y="99" width="92" height="17" fill="var(--blue)"/>
      <text x="157" y="110">8,2</text>
      <text x="56" y="146" text-anchor="end">2nd Qtr</text>
      <rect x="62" y="135" width="35" height="17" fill="#a6a6a6"/>
      <text x="100" y="146">3,2</text>
      <text x="56" y="182" text-anchor="end">3rd Qtr</text>
      <rect x="62" y="171" width="15" height="17" fill="#a6a6a6"/>
      <text x="80" y="182">1,4</text>
      <text x="56" y="218" text-anchor="end">4th Qtr</text>
      <rect x="62" y="207" width="13" height="17" fill="#a6a6a6"/>
      <text x="78" y="218">1,2</text>
    </g>
  </svg>
  <ul class="bullets" style="position:absolute;left:195px;top:96px;width:150px;display:flex;flex-direction:column;gap:6px">
    <li>Lorem ipsum dolor sit amet, consectetur adipiscing elit. Duis blandit lorem eu libero congue aliquam vel sit amet augue. Mauris augue ipsum, dignissim vitae adipiscing eu, euismod nec sem.</li>
    <li>Lorem ipsum dolor sit amet, consectetur adipiscing elit. Duis blandit lorem eu libero congue aliquam vel sit amet augue. Mauris augue ipsum, dignissim vitae adipiscing eu, euismod nec sem.</li>
  </ul>
  <div class="brand footer-brand"><span class="dot"></span>Quorvian</div>
  <div class="copyright">© 2013 Quorvian Technologies. All rights reserved</div>
  <div class="page-no">7</div>
</section>

<!-- Graph slide 2: lines -->
<section class="slide c3 r2">
  <h2 class="slide-title" style="font-weight:400">Graph Slide – Example 2</h2>
  <svg width="373" height="280" style="position:absolute;left:0;top:0" aria-label="Line chart of sales and gross margin by quarter">
    <line x1="30" y1="230" x2="352" y2="230" stroke="#ccc" stroke-width=".6"/>
    <g font-size="5" fill="#555" text-anchor="middle">
      <text x="70" y="241">4th Qtr</text><text x="147" y="241">3rd Qtr</text>
      <text x="225" y="241">2nd Qtr</text><text x="302" y="241">1st Qtr</text>
    </g>
    <polyline points="70,162 147,174 225,113 302,147" fill="none" stroke="var(--orange)" stroke-width="1.2"/>
    <polyline points="70,211 147,208 225,180 302,103" fill="none" stroke="var(--blue)" stroke-width="1.2"/>
    <g fill="#fff" stroke-width="1">
      <circle cx="70" cy="162" r="2" stroke="var(--orange)"/><circle cx="147" cy="174" r="2" stroke="var(--orange)"/>
      <circle cx="225" cy="113" r="2" stroke="var(--orange)"/><circle cx="302" cy="147" r="2" stroke="var(--orange)"/>
      <circle cx="70" cy="211" r="2" stroke="var(--blue)"/><circle cx="147" cy="208" r="2" stroke="var(--blue)"/>
      <circle cx="225" cy="180" r="2" stroke="var(--blue)"/><circle cx="302" cy="103" r="2" stroke="var(--blue)"/>
    </g>
    <g font-size="5" fill="#333" text-anchor="middle">
      <text x="70" y="156">4,4</text><text x="147" y="168">3,6</text><text x="225" y="107">7,5</text><text x="302" y="141">5,3</text>
      <text x="70" y="205">1,2</text><text x="147" y="202">1,4</text><text x="225" y="174">3,2</text><text x="302" y="97">8,2</text>
    </g>
    <path d="M70 94h70a2 2 0 0 1 2 2v32a2 2 0 0 1-2 2H108l-5 5-5-5H70a2 2 0 0 1-2-2V96a2 2 0 0 1 2-2z" fill="var(--orange)"/>
    <text x="105" y="110" font-size="6" fill="#fff" text-anchor="middle">Positive overall</text>
    <text x="105" y="119" font-size="6" fill="#fff" text-anchor="middle">trend for sales</text>
    <path d="M247 186h30l5-5 5 5h52a2 2 0 0 1 2 2v31a2 2 0 0 1-2 2H247a2 2 0 0 1-2-2v-31a2 2 0 0 1 2-2z" fill="var(--blue)"/>
    <text x="293" y="202" font-size="6" fill="#fff" text-anchor="middle">Positive overall trend</text>
    <text x="293" y="211" font-size="6" fill="#fff" text-anchor="middle">for gross margin</text>
  </svg>
  <div class="brand footer-brand"><span class="dot"></span>Quorvian</div>
  <div class="copyright">© 2013 Quorvian Technologies. All rights reserved</div>
  <div class="page-no">8</div>
</section>

<!-- Graph slide: donut -->
<section class="slide c1 r3">
  <h2 class="slide-title" style="font-weight:400">Graph Slide – Example 2</h2>
  <svg width="373" height="280" style="position:absolute;left:0;top:0" aria-label="Donut chart of quarterly share">
    <g transform="rotate(-90 90 141)" fill="none" stroke-width="34">
      <circle cx="90" cy="141" r="49" stroke="var(--blue)" stroke-dasharray="180.3 307.9"/>
      <circle cx="90" cy="141" r="49" stroke="#a6a6a6" stroke-dasharray="0 180.3 70.4 307.9"/>
      <circle cx="90" cy="141" r="49" stroke="#8c8c8c" stroke-dasharray="0 250.7 30.8 307.9"/>
      <circle cx="90" cy="141" r="49" stroke="#7a7a7a" stroke-dasharray="0 281.5 26.4 307.9"/>
    </g>
    <g font-size="5.5" text-anchor="middle">
      <text x="138" y="155" fill="#fff">8,2</text>
      <text x="43" y="163" fill="#fff">3,2</text>
      <text x="51" y="113" fill="#eee">1,4</text>
      <text x="76" y="98" fill="#eee">1,2</text>
    </g>
  </svg>
  <ul class="bullets" style="position:absolute;left:184px;top:79px;width:155px;font-size:6px;display:flex;flex-direction:column;gap:6px">
    <li>Lorem ipsum dolor sit amet, consectetur adipiscing elit. Duis blandit lorem eu libero congue aliquam vel sit amet augue. Mauris augue ipsum, dignissim vitae adipiscing eu, euismod nec sem.</li>
    <li>Lorem ipsum dolor sit amet, consectetur adipiscing elit. Duis blandit lorem eu libero congue aliquam vel sit amet augue. Mauris augue ipsum, dignissim vitae adipiscing eu, euismod nec sem.</li>
  </ul>
  <div class="brand footer-brand"><span class="dot"></span>Quorvian</div>
  <div class="copyright">© 2013 Quorvian Technologies. All rights reserved</div>
  <div class="page-no">6</div>
</section>

<!-- Summary -->
<section class="slide c2 r3">
  <div style="position:absolute;left:0;top:32px;width:44px;height:19px;background:var(--blue);color:#fff;font-size:5.5px;display:flex;align-items:center;justify-content:center">Summary</div>
  <ol style="list-style:none;position:absolute;left:50px;top:62px;width:300px;font-size:5.5px;line-height:1.55;display:flex;flex-direction:column;gap:5px">
    <li style="display:flex;gap:7px"><span style="flex:none;width:13px;height:13px;border-radius:50%;background:var(--blue);color:#fff;font-size:5px;font-weight:700;display:flex;align-items:center;justify-content:center;margin-top:1px">1</span><span>Lorem ipsum dolor sit amet, consectetur adipiscing elit. Duis blandit lorem eu libero congue aliquam vel sit amet augue. Mauris augue ipsum, dignissim vitae adipiscing eu, euismod nec sem.</span></li>
    <li style="display:flex;gap:7px"><span style="flex:none;width:13px;height:13px;border-radius:50%;background:var(--blue);color:#fff;font-size:5px;font-weight:700;display:flex;align-items:center;justify-content:center;margin-top:1px">2</span><span>Lorem ipsum dolor sit amet, consectetur adipiscing elit. Duis blandit lorem eu libero congue aliquam vel sit amet augue. Mauris augue ipsum, dignissim vitae adipiscing eu, euismod nec sem.</span></li>
    <li style="display:flex;gap:7px"><span style="flex:none;width:13px;height:13px;border-radius:50%;background:var(--blue);color:#fff;font-size:5px;font-weight:700;display:flex;align-items:center;justify-content:center;margin-top:1px">3</span><span>Lorem ipsum dolor sit amet, consectetur adipiscing elit. Duis blandit lorem eu libero congue aliquam vel sit amet augue. Mauris augue ipsum, dignissim vitae adipiscing eu, euismod nec sem.</span></li>
    <li style="display:flex;gap:7px"><span style="flex:none;width:13px;height:13px;border-radius:50%;background:var(--blue);color:#fff;font-size:5px;font-weight:700;display:flex;align-items:center;justify-content:center;margin-top:1px">4</span><span>Lorem ipsum dolor sit amet, consectetur adipiscing elit. Duis blandit lorem eu libero congue aliquam vel sit amet augue. Mauris augue ipsum, dignissim vitae adipiscing eu, euismod nec sem.</span></li>
    <li style="display:flex;gap:7px"><span style="flex:none;width:13px;height:13px;border-radius:50%;background:var(--blue);color:#fff;font-size:5px;font-weight:700;display:flex;align-items:center;justify-content:center;margin-top:1px">5</span><span>Lorem ipsum dolor sit amet, consectetur adipiscing elit. Duis blandit lorem eu libero congue aliquam vel sit amet augue. Mauris augue ipsum, dignissim vitae adipiscing eu, euismod nec sem.</span></li>
  </ol>
  <div class="brand footer-brand"><span class="dot"></span>Quorvian</div>
  <div class="copyright">© 2013 Quorvian Technologies. All rights reserved</div>
  <div class="page-no">9</div>
</section>

<!-- Closing slide -->
<section class="slide c3 r3">
  <div style="position:absolute;left:80px;top:80px;width:207px;height:68px;background:linear-gradient(180deg,#f2f2f2,#e2e2e2);box-shadow:0 3px 5px rgba(0,0,0,.25);display:flex;flex-direction:column;align-items:center;justify-content:center;gap:10px">
    <div class="brand" style="font-size:15px;color:#1f1f1f"><span class="dot" style="width:12px;height:12px"></span>Quorvian</div>
    <div class="url" style="color:#aaa">www.quorvian.example</div>
  </div>
  <p style="position:absolute;top:184px;width:100%;text-align:center;font-size:9px;font-weight:700;color:var(--blue)">Thank You For Your Time!</p>
  <div class="copyright">© 2013 Quorvian Technologies. All rights reserved</div>
</section>

</body>
</html>
```